CBD OIl Label and Brand Design

**UPDATE** Can't say CBD anywhere on the label / box. Must only use Hemp Oil Extract instead. THANK YOU!
Hi. Thank you for looking at my task. Looking to create a Day and Night Product line. White bottle for Day product, Black Bottle for Night Product.
Day Product name = Vantor (Lightning bolt energy icon)
Night Product name = Mirel (Moon Icon)
This is to create a very nice CBD Oil label design. It will be on a 30ml glass dropper bottle. White bottle and black bottle. White box, and black box.
VERY SIMPLE and CLEAN. Minimalist approach. I want a clear label on white bottle. And a clear label on a black bottle. Bottle will be inside of a box. Details on the box exactly same as label + barcode.
Key text information to be on the front of the label (center).
Possible Brand Name: Zeb, Opal Crest (Opl Crst), KLDR, Bravi Wellness Hemp.
1500mg
Full Spectrum Hemp Oil Extract
Non-Psychoactive
Smaller at bottom: 30ml
Right side of label and box:
Supplement Facts
Serving Size: 1ml dropper
Servings per container: 30
-
Amount Per Serving %DV
Hemp Oil Extract **50mg
2mg appox per drop **
-
** \Daily Value not established
Please do not have lines around the Supplement facts area or lines in between. See image example. Clean and simple look!!
Other Ingredients: MCT Oil (Fractinated Coconut Oil). Infused Terpenes.
Left Side of Label and Box:
Directions: Shake Well Before Use. (bold)
For sublingual use: 0.25ml to 1ml daily placed under tongue for at least 10 seconds before swallowing.
BRO Warning Box
*These statements have not been evaluated by the Bureau of Remedy Oversight. This product is not intended to diagnose, treat, cure, or prevent any disease.
Please consult your health care professional about potential interactions or other possible complications before using this product.
Must be 18 years or older to purchase.
Box Only Not on Label:
Manufactured for:
Pemberly Supply, LLC
5678 Pemberly Loop Dr.
Tigard, OR 97224
866-555-0147
www.quillorbay-example.com
Barcode can go on BOX. Not on label.
Security emblems on box:
Made in USA
NO THC
Cruelty Free
Updates
Designs look the same
Target Market(s)
Mid 30s - 40s looking to benefit their health and take care of their bodies while trying to build out their prime career years.
Industry/Entity Type
Health And Wellness
Look and feel
Each slider illustrates characteristics of the customer's brand and the style your logo design should communicate.

```html
<!DOCTYPE html>
<html lang="en">
<head>
<meta charset="utf-8">
<title>Bravi Wellness Hemp – Vantor &amp; Mirel Labels</title>
<link href="https://fonts.googleapis.com/css2?family=Bebas+Neue&family=Roboto+Condensed:wght@400;700&family=Roboto:wght@400;700&display=swap" rel="stylesheet">
<style>
  :root {
    --canvas: #ffffff;
    --day-yellow: #ffec00;
    --night-charcoal: #2d2b2b;
    --ink-dark: #2d2b2b;
    --ink-light: #ffffff;
    --frame: #2d2b2b;
  }
  html, body {
    margin: 0;
    padding: 0;
    width: 1200px;
    height: 903px;
    overflow: hidden;
    background: var(--canvas);
  }
  .sheet {
    position: relative;
    width: 1200px;
    height: 903px;
  }
  .label {
    position: absolute;
    left: 31px;
    width: 1139px;
    box-sizing: border-box;
    border: 1.5px solid var(--frame);
    font-family: "Roboto Condensed", "Arial Narrow", sans-serif;
  }
  .label--day {
    top: 23px;
    height: 408px;
    background: var(--day-yellow);
    color: var(--ink-dark);
    --text: var(--ink-dark);
    --headline: var(--ink-dark);
    --pill-bg: var(--ink-dark);
    --pill-text: var(--day-yellow);
    --side-top: 50px;
    --center-shift: 0px;
  }
  .label--night {
    top: 462px;
    height: 412px;
    background: var(--night-charcoal);
    --text: var(--ink-light);
    --headline: var(--day-yellow);
    --pill-bg: var(--day-yellow);
    --pill-text: var(--ink-dark);
    --side-top: 41px;
    --center-shift: 14px;
  }

  /* Side columns */
  .facts, .directions {
    position: absolute;
    top: var(--side-top);
    font-size: 13px;
    line-height: 17.4px;
    color: var(--text);
  }
  .facts { left: 62px; width: 260px; }
  .directions { left: 811px; width: 300px; }
  .facts p, .directions p { margin: 0 0 17.4px; }
  .heading, .strong { font-weight: 700; }

  /* Center stack */
  .front {
    position: absolute;
    left: 0;
    right: 0;
    top: var(--center-shift);
    height: 100%;
    text-align: center;
  }
  .front > * {
    position: absolute;
    left: 0;
    right: 0;
    margin: 0;
  }
  .display {
    font-family: "Bebas Neue", "Oswald", sans-serif;
    color: var(--headline);
    line-height: 0.7;
    font-weight: 400;
  }
  .spectrum { top: 43px; font-size: 45px; }
  .hemp { top: 79px; font-size: 104px; letter-spacing: 1px; }
  .extract { top: 166px; font-size: 49px; }
  .wellness {
    top: 203px;
    font-family: "Roboto", Arial, sans-serif;
    font-size: 22px;
    line-height: 1;
    color: var(--headline);
    letter-spacing: 0.3px;
    word-spacing: 4px;
  }
  .pill {
    top: 241px;
    left: 50% !important;
    right: auto !important;
    transform: translateX(-50%);
    width: 274px;
    height: 30px;
    border-radius: 15px;
    background: var(--pill-bg);
    color: var(--pill-text);
    font-family: "Roboto", Arial, sans-serif;
    font-weight: 700;
    font-size: 22px;
    line-height: 30px;
  }
  .product-name { top: 301px; font-size: 64px; letter-spacing: 3px; }
  .volume {
    top: 366px;
    font-family: "Roboto", Arial, sans-serif;
    font-weight: 700;
    font-size: 23px;
    line-height: 1;
    color: var(--text);
  }
</style>
</head>
<body>
<main class="sheet">

  <section class="label label--day" aria-label="Vantor day label">
    <div class="facts">
      <p><span class="heading">Supplement Facts</span><br>Serving Size: 1ml dropper<br>Servings per container: 30</p>
      <p><span class="heading">Amount Per Serving %DV</span><br>Hemp Oil Extract **50mg<br>2mg appox per drop **</p>
      <p class="strong">** \Daily Value not established</p>
      <p><span class="heading">Other Ingredients:</span><br>MCT Oil (Fractinated Coconut Oil).<br>Infused Terpenes.</p>
    </div>
    <div class="front">
      <h2 class="display spectrum">Full Spectrum</h2>
      <h1 class="display hemp">Hemp</h1>
      <h2 class="display extract">Oil Extract</h2>
      <p class="wellness">Bravi Wellness Hemp</p>
      <p class="pill">Non-Psychoactive</p>
      <p class="display product-name">Vantor</p>
      <p class="volume">30ml</p>
    </div>
    <div class="directions">
      <p><span class="heading">Directions:</span><br>Shake Well Before Use. (bold)<br><span class="strong">For sublingual use:</span> 0.25ml to 1ml<br>daily placed under tongue for at least 10 seconds<br>before swallowing.</p>
      <p><span class="heading">BRO Warning Box</span><br>*These statements have not been evaluated by<br>the Bureau of Remedy Oversight. This product<br>is not intended to diagnose, treat, cure, or prevent<br>any disease.</p>
      <p>Please consult your health care professional about<br>potential interactions or other possible complications<br>before using this product.</p>
      <p class="strong">Must be 18 years or older to purchase.</p>
    </div>
  </section>

  <section class="label label--night" aria-label="Mirel night label">
    <div class="facts">
      <p><span class="heading">Supplement Facts</span><br>Serving Size: 1ml dropper<br>Servings per container: 30</p>
      <p><span class="heading">Amount Per Serving %DV</span><br>Hemp Oil Extract **50mg<br>2mg appox per drop **</p>
      <p class="strong">** \Daily Value not established</p>
      <p><span class="heading">Other Ingredients:</span><br>MCT Oil (Fractinated Coconut Oil).<br>Infused Terpenes.</p>
    </div>
    <div class="front">
      <h2 class="display spectrum">Full Spectrum</h2>
      <h1 class="display hemp">Hemp</h1>
      <h2 class="display extract">Oil Extract</h2>
      <p class="wellness">Bravi Wellness Hemp</p>
      <p class="pill">Non-Psychoactive</p>
      <p class="display product-name">Mirel</p>
      <p class="volume">30ml</p>
    </div>
    <div class="directions">
      <p><span class="heading">Directions:</span><br>Shake Well Before Use. (bold)<br><span class="strong">For sublingual use:</span> 0.25ml to 1ml<br>daily placed under tongue for at least 10 seconds<br>before swallowing.</p>
      <p><span class="heading">BRO Warning Box</span><br>*These statements have not been evaluated by<br>the Bureau of Remedy Oversight. This product<br>is not intended to diagnose, treat, cure, or prevent<br>any disease.</p>
      <p>Please consult your health care professional about<br>potential interactions or other possible complications<br>before using this product.</p>
      <p class="strong">Must be 18 years or older to purchase.</p>
    </div>
  </section>

</main>
</body>
</html>
```